Business Card for Makeup Artist

I need a business card designed for my makeup and hair artistry business which is primarily events and weddings focused. The card needs to be sleek, simple, stylish and appealing to women. I would prefer a white background but open to suggestions also. I also love the marble background look. I have attached some example pics. It needs to be a double sided card with logo and/or design on one side and contact details in the centre of the card on the other side. NO LOGO ON BACK. Examples attached.

Target Market(s)

Females age 14-55

Industry/Entity Type

Business

Contact Information for Business Card

Nora Pelling
Principal Makeup Artist
P: 0412 903 251
E: nora@lumivamakeup.com.au
W: www.lumivamakeup.com.au

Requirements
Should not have
• No yellow, green, red or blue in the design.

```html
<!DOCTYPE html>
<html lang="en">
<head>
<meta charset="utf-8">
<title>Lumiva Makeup Artistry – Business Card</title>
<link rel="stylesheet" href="https://fonts.googleapis.com/css2?family=Pinyon+Script&family=Jost:wght@300;400&family=Arimo&display=swap">
<style>
  :root {
    --stage: #3b3b3b;
    --card-base: #f1f1ef;
    --vein-light: #e2e2e0;
    --vein-mid: #d4d4d2;
    --ink: #5a5a5a;
    --ink-soft: #6a6a6a;
    --accent: #e85bc8;
  }
  * { margin: 0; padding: 0; box-sizing: border-box; }
  html, body { width: 1200px; height: 750px; overflow: hidden; }
  body { background: var(--stage); position: relative; }

  .card {
    position: absolute;
    top: 228px;
    width: 461px;
    height: 263px;
    overflow: hidden;
    background: var(--card-base);
  }
  .card--front { left: 124px; }
  .card--back { left: 618px; }

  .marble {
    position: absolute; inset: 0;
    background:
      linear-gradient(150deg, transparent 0 18%, var(--vein-mid) 24%, transparent 32%),
      linear-gradient(155deg, transparent 0 45%, var(--vein-light) 52%, transparent 60%),
      linear-gradient(150deg, transparent 0 68%, var(--vein-mid) 76%, transparent 84%),
      radial-gradient(ellipse at 15% 30%, var(--vein-mid), transparent 55%),
      linear-gradient(135deg, #f6f6f4, var(--card-base) 50%, #e8e8e6);
    opacity: .9;
  }

  .brand {
    position: absolute;
    left: 0; right: 0;
    top: 62px;
    text-align: center;
    color: var(--ink);
  }
  .brand__name {
    display: block;
    font-family: "Pinyon Script", cursive;
    font-size: 86px;
    line-height: 1;
  }
  .brand__tagline {
    display: block;
    margin-top: 2px;
    margin-left: 70px;
    font-family: "Jost", sans-serif;
    font-weight: 300;
    font-size: 20px;
    letter-spacing: .5px;
  }

  .person {
    position: absolute;
    left: 36px;
    top: 176px;
  }
  .person__name {
    font-family: "Pinyon Script", cursive;
    font-size: 38px;
    line-height: 1;
    color: var(--ink);
  }
  .person__role {
    margin-top: 2px;
    font-family: "Jost", sans-serif;
    font-weight: 300;
    font-size: 12.5px;
    color: var(--accent);
    letter-spacing: .2px;
  }

  .divider {
    position: absolute;
    left: 238px;
    top: 192px;
    width: 1.5px;
    height: 46px;
    background: var(--ink-soft);
  }

  .contact {
    position: absolute;
    left: 254px;
    top: 192px;
    list-style: none;
    font-family: "Arimo", sans-serif;
    font-size: 12px;
    color: var(--ink-soft);
  }
  .contact__item {
    display: flex;
    align-items: center;
    height: 15.5px;
  }
  .contact__icon {
    width: 10px; height: 10px;
    margin-right: 7px;
    fill: var(--ink);
  }
</style>
</head>
<body>

<section class="card card--front">
  <div class="marble" role="img" aria-label="Soft white and grey marble texture"></div>
  <div class="brand">
    <span class="brand__name">Lumiva</span>
    <span class="brand__tagline">MAKEUP ARTISTRY</span>
  </div>
</section>

<section class="card card--back">
  <div class="marble" role="img" aria-label="Soft white and grey marble texture"></div>
  <div class="person">
    <p class="person__name">Nora Pelling</p>
    <p class="person__role">PRINCIPAL MAKEUP ARTIST</p>
  </div>
  <div class="divider"></div>
  <ul class="contact">
    <li class="contact__item">
      <svg class="contact__icon" viewBox="0 0 10 10" aria-hidden="true"><path d="M2 0.5 L3.6 2.6 L2.7 3.7 Q3.6 5.8 6.3 7.3 L7.4 6.4 L9.5 8 L8.3 9.5 Q1 8 0.5 1.7 Z"/></svg>
      0412 903 251
    </li>
    <li class="contact__item">
      <svg class="contact__icon" viewBox="0 0 10 10" aria-hidden="true"><path d="M0.5 2 H9.5 V8.5 H0.5 Z" /><path d="M0.8 2.4 L5 5.6 L9.2 2.4" stroke="#f1f1ef" stroke-width="1" fill="none"/></svg>
      nora@lumivamakeup.com.au
    </li>
    <li class="contact__item">
      <svg class="contact__icon" viewBox="0 0 10 10" aria-hidden="true"><circle cx="5" cy="5" r="4.6"/><path d="M0.6 5 H9.4 M5 0.5 Q2.5 5 5 9.5 M5 0.5 Q7.5 5 5 9.5" stroke="#f1f1ef" stroke-width=".8" fill="none"/></svg>
      www.lumivamakeup.com.au
    </li>
  </ul>
</section>

</body>
</html>
```